Cleaning Company Website Design

I am looking for a website design that has my contact information on each page (Call or Text and my e-mail). It should have the main landing page and than pages for Residential Cleaning (Move In/Move Out, Weekly, and Bi-Weekly Cleaning), Commercial Cleaning (Move In/Move Out, Weekly, and Bi-Weekly Cleaning), New Construction Cleaning (Residential, Commercial, and Industrial), and Apartment Turn cleaning for Property Managers. It should list that we carry insurance as well.

Target Market(s)

Residential and Commercial Customers

Industry/Entity Type

Cleaning

Coding

Coded - Design and coding required

Number of Pages Required

5+ page

Requirements
Must have
• A clean professional looking website

```html
<!DOCTYPE html>
<html lang="en">
<head>
<meta charset="utf-8">
<title>Brightway Cleaning – Website Design</title>
<link href="https://fonts.googleapis.com/css2?family=Poppins:wght@400;500;600;700;800&display=swap" rel="stylesheet">
<style>
:root{
  --board:#e9f1fc;
  --teal:#2fb5a6;
  --teal-dark:#118a82;
  --blue:#2a86cc;
  --navy:#0c3d86;
  --deep:#0a2f80;
  --ink:#1f2a37;
  --muted:#7b8593;
  --card:#ffffff;
  --pale:#eef5fd;
  --line:#d7dfe9;
}
*{margin:0;padding:0;box-sizing:border-box}
html,body{width:1200px;height:3125px;overflow:hidden;background:var(--board);font-family:'Poppins',sans-serif;color:var(--ink)}
.board{position:relative;width:1200px;height:3125px}
.abs{position:absolute}
.brand{font-family:'Poppins',sans-serif;font-weight:700;color:var(--teal-dark);letter-spacing:.04em;white-space:nowrap;display:flex;align-items:center;gap:8px}
.brand .dot{display:inline-block;background:var(--blue);border-radius:50%}
.board-brand{left:0;width:1200px;top:76px;justify-content:center;font-size:34px}
.board-brand .dot{width:22px;height:22px}
.site{left:120px;top:201px;width:960px;height:2819px;background:#fff;box-shadow:0 10px 40px rgba(30,70,130,.12);overflow:hidden}
.site section,.site header,.site nav,.site footer{position:absolute;left:0;width:960px}
/* header */
.topbar{top:0;height:50px;background:#fff}
.topbar .brand{left:138px;top:17px;font-size:12px;position:absolute}
.topbar .brand .dot{width:9px;height:9px}
.contact{position:absolute;top:14px;display:flex;align-items:center;gap:6px}
.ico{width:23px;height:23px;border:1.5px solid var(--blue);border-radius:50%;display:flex;align-items:center;justify-content:center;flex:none}
.contact b{display:block;font-size:7px;color:var(--blue);font-weight:600}
.contact span{display:block;font-size:7px;color:var(--ink)}
.vline{position:absolute;top:14px;width:1px;height:24px;background:var(--line)}
.btn{position:absolute;background:var(--teal);color:#fff;font-size:8px;font-weight:600;display:flex;align-items:center;justify-content:center;gap:6px;border-radius:1px;text-transform:uppercase}
.mainnav{top:50px;height:35px;background:var(--blue)}
.mainnav a{position:absolute;top:0;height:35px;line-height:35px;color:#fff;font-size:10px;text-decoration:none;text-transform:uppercase}
.mainnav .active{background:var(--teal);left:138px;width:95px;text-align:center}
/* hero */
.hero{top:85px;height:384px;background:linear-gradient(90deg,#f4f6f8 0%,#fbfcfd 55%,#fff 100%)}
.hero h1{position:absolute;left:138px;top:104px;width:380px;font-size:23px;line-height:30px;font-weight:700;color:var(--navy);white-space:nowrap;letter-spacing:-.01em}
.hero h1 em{font-style:normal;color:var(--teal-dark)}
.hero p{position:absolute;left:138px;top:203px;width:350px;font-size:8.5px;line-height:13px}
.photo{position:absolute}
/* section titles */
.sec-title{position:absolute;left:0;width:960px;text-align:center;font-size:14.5px;font-weight:600}
.mark{position:absolute;left:468px;width:24px;height:24px;border-radius:50%;background:var(--blue)}
.why{top:469px;height:291px;background:var(--pale)}
.feat{position:absolute;top:120px;width:221px;height:115px;background:#fff;text-align:center;box-shadow:0 3px 12px rgba(40,80,140,.06)}
.feat svg{margin-top:22px}
.feat h3{font-size:11px;font-weight:600;margin-top:10px}
.feat p{font-size:7.5px;color:var(--muted);line-height:10px;margin:4px 14px 0}
/* about */
.about{top:760px;height:419px;background:#fff}
.about .kicker{position:absolute;left:450px;top:120px;font-size:7.5px;color:var(--teal);font-weight:600;display:flex;align-items:center;gap:4px}
.about .kicker i{display:inline-block;width:22px;height:1px;background:var(--teal)}
.about h2{position:absolute;left:450px;top:131px;font-size:15.5px;font-weight:600}
.about p{position:absolute;left:450px;width:370px;font-size:8.5px;line-height:13.4px}
/* services */
.services{top:1179px;height:587px;background:linear-gradient(180deg,#f5f8fc 0%,#eef3f8 100%)}
.svc{position:absolute;width:221px;height:187px;background:#fff;text-align:center}
.svc .pic{width:36px;height:36px;margin:22px auto 0;border-radius:6px}
.svc h3{font-size:12px;font-weight:600;margin-top:16px}
.svc p{font-size:8px;color:var(--muted);line-height:11px;margin:3px 24px 0}
.svc .go{position:absolute;left:95px;bottom:22px;width:31px;height:23px;background:var(--teal);display:flex;align-items:center;justify-content:center}
.promo{position:absolute;left:369px;top:317px;width:451px;height:187px;background:linear-gradient(90deg,#1b5fa6,#1f6fb5)}
.promo h3{position:absolute;left:129px;top:49px;color:#fff;font-size:12px;font-weight:600}
.promo p{position:absolute;left:129px;top:67px;width:290px;color:#dce9f7;font-size:8px;line-height:11px}
/* how it works */
.how{top:1766px;height:209px;background:linear-gradient(100deg,#0a2a7c 0%,#0b3f8e 45%,#0c6e8c 80%,#0e8a86 100%)}
.how h2{position:absolute;left:0;width:960px;top:37px;text-align:center;color:#fff;font-size:14px;font-weight:600}
.step{position:absolute;top:71px;width:160px;text-align:center;color:#fff}
.step .box{width:42px;height:40px;margin:0 auto;background:var(--teal);border-radius:3px;display:flex;align-items:center;justify-content:center}
.step h3{font-size:10px;font-weight:500;margin-top:14px}
.step p{font-size:7px;line-height:10px;color:#b9cbe6;margin-top:2px}
.dash{position:absolute;top:91px;height:0;border-top:1px dashed #c9d6ee}
/* testimonials */
.reviews{top:1975px;height:408px;background:#fff}
.review{position:absolute;top:121px;width:210px;background:#fff;box-shadow:0 4px 16px rgba(30,60,110,.12);text-align:center}
.avatar{width:80px;height:80px;border-radius:50%;margin:11px auto 0}
.review h4{font-size:6.5px;font-weight:600;margin-top:11px}
.review small{display:block;font-size:5.5px;color:var(--muted)}
.stars{color:#3567d6;font-size:11px;letter-spacing:1px;margin-top:6px}
.review p{font-size:8px;line-height:12px;margin:5px 10px 0}
.tag{font-size:4.5px;color:var(--muted);margin:6px 0 10px;display:flex;justify-content:center;align-items:center;gap:3px}
.tag i{width:5px;height:5px;border-radius:50%;background:#6a4fe0;display:inline-block}
.arrow{position:absolute;top:215px;width:32px;height:22px;background:var(--teal);display:flex;align-items:center;justify-content:center}
/* commitment */
.commit{top:2383px;height:210px;background:linear-gradient(180deg,#0f8c88 0%,#126aa0 100%)}
.commit h2{position:absolute;left:138px;top:55px;width:420px;color:#fff;font-size:21px;line-height:25px;font-weight:500}
.commit h2 em{font-style:normal;font-weight:600;color:#6fe0d5}
.commit p{position:absolute;left:138px;top:108px;color:#e0f2f2;font-size:8.5px}
/* footer */
.foot{top:2593px;height:226px;background:#f6f7f9}
.foot .brand{position:absolute;left:0;width:960px;top:44px;justify-content:center;font-size:22px}
.foot .brand .dot{width:13px;height:13px}
.foot-links{position:absolute;left:0;width:960px;top:134px;display:flex;justify-content:center;gap:26px;font-size:9px}
.hr{position:absolute;left:138px;width:682px;height:1px;background:var(--line)}
.copy{position:absolute;left:0;width:960px;top:211px;text-align:center;font-size:7.5px;color:var(--muted)}
.thanks{left:0;width:1200px;top:3055px;text-align:center;font-size:27px;font-weight:700;color:var(--deep)}
</style>
</head>
<body>
<div class="board">
  <div class="abs brand board-brand"><span class="dot"></span>BRIGHTWAY CLEANING</div>

  <main class="abs site">
    <header class="topbar">
      <div class="brand"><span class="dot"></span>BRIGHTWAY</div>
      <div class="contact" style="left:248px">
        <div class="ico"><svg width="11" height="9" viewBox="0 0 11 9"><rect x=".5" y=".5" width="10" height="8" fill="none" stroke="#2a86cc"/><path d="M.5 .5l5 4 5-4" fill="none" stroke="#2a86cc"/></svg></div>
        <div><b>MAIL US</b><span>hello@brightwaycleaning.com</span></div>
      </div>
      <div class="vline" style="left:398px"></div>
      <div class="contact" style="left:416px">
        <div class="ico"><svg width="11" height="11" viewBox="0 0 11 11"><circle cx="5.5" cy="5.5" r="5" fill="#2a86cc"/><path d="M5.5 2.5v3l2 1.3" stroke="#fff" fill="none"/></svg></div>
        <div><b>BUSINESS HOURS</b><span>9:00 AM - 7:00 PM Mon-Sat</span></div>
      </div>
      <div class="vline" style="left:562px"></div>
      <div class="contact" style="left:580px">
        <div class="ico"><svg width="11" height="11" viewBox="0 0 24 24"><path d="M6.6 10.8a15 15 0 006.6 6.6l2.2-2.2c.3-.3.7-.4 1-.2 1.1.4 2.3.6 3.6.6.6 0 1 .4 1 1V20c0 .6-.4 1-1 1C10.6 21 3 13.4 3 4c0-.6.4-1 1-1h3.5c.6 0 1 .4 1 1 0 1.3.2 2.5.6 3.6.1.3 0 .7-.2 1z" fill="#2a86cc"/></svg></div>
        <div><b>CALL US TODAY</b><span>(555) 014-2290</span></div>
      </div>
      <div class="btn" style="left:726px;top:10px;width:94px;height:29px">Book Now</div>
    </header>

    <nav class="mainnav">
      <a class="active">⌂ Home</a>
      <a style="left:259px">About Us</a>
      <a style="left:356px">Service</a>
      <a style="left:444px">Service Area</a>
      <a style="left:559px">Review</a>
      <a style="left:644px">Pricing</a>
      <a style="left:733px">Contact Us</a>
    </nav>

    <section class="hero">
      <h1><em>Quality Driven and</em><br><em>Reliable</em> to Take Care of All<br>Your Cleaning Needs!!!</h1>
      <p>As a leading provider of cleaning services, we take pride in offering the best professional service.</p>
      <div class="btn" style="left:138px;top:244px;width:95px;height:29px">Book Now</div>
      <div class="btn" style="left:243px;top:244px;width:114px;height:29px"><svg width="12" height="12" viewBox="0 0 12 12"><circle cx="6" cy="6" r="6" fill="#fff"/><path d="M4 3.5l1 .1.5 1.4-.7.6a4 4 0 001.7 1.7l.6-.7 1.4.5.1 1c-2.7.3-5-2-4.6-4.6z" fill="#2fb5a6"/></svg>(555) 014-2290</div>
      <div class="photo" role="img" aria-label="Collage of three framed photos of cleaners at work: team cleaning an office, a worker mopping a floor, a man washing a glass window" style="left:511px;top:39px;width:364px;height:312px">
        <svg width="364" height="312" viewBox="0 0 364 312">
          <defs><linearGradient id="ph" x1="0" y1="0" x2="0" y2="1"><stop offset="0" stop-color="#cfe0f0"/><stop offset="1" stop-color="#6a9ccd"/></linearGradient></defs>
          <polygon points="0,20 145,0 180,250 40,265" fill="url(#ph)" stroke="#2a86cc" stroke-width="3"/>
          <polygon points="205,5 345,20 300,272 170,250" fill="url(#ph)" stroke="#2a86cc" stroke-width="3"/>
          <polygon points="115,45 238,40 268,285 135,305" fill="#9cc1e2" stroke="#2fb5a6" stroke-width="4"/>
        </svg>
      </div>
    </section>

    <section class="why">
      <div class="mark" style="top:56px"></div>
      <h2 class="sec-title" style="top:86px">Why Book Your Cleaning Service with Us?</h2>
      <div class="feat" style="left:138px"><svg width="14" height="14" viewBox="0 0 14 14"><path d="M1 6h3v7H1zM5 6l3-5c1 0 2 1 1.5 2.5L9 5h3.5c.8 0 1.3.8 1 1.5l-2 5.5c-.2.6-.7 1-1.3 1H5z" fill="#2a86cc"/></svg><h3>Simple</h3><p>Lorem ipsum dolor sit amet consectetur. Massa lacus imperdiet sed neque nunc diam pellentesque.</p></div>
      <div class="feat" style="left:369px"><svg width="14" height="14" viewBox="0 0 14 14"><path d="M7 0l6 2.5v4C13 10 10.5 12.8 7 14 3.5 12.8 1 10 1 6.5v-4z" fill="#2a86cc"/><path d="M4.5 7l2 2 3-3.5" stroke="#fff" stroke-width="1.4" fill="none"/></svg><h3>Highly Trusted</h3><p>Lorem ipsum dolor sit amet consectetur. Massa lacus imperdiet sed neque nunc diam pellentesque.</p></div>
      <div class="feat" style="left:599px"><svg width="14" height="14" viewBox="0 0 14 14"><rect x="2" y="3" width="10" height="10" rx="2" fill="#2a86cc"/><rect x="5" y="0.5" width="4" height="3" fill="#2a86cc"/><path d="M5 8l1.5 1.5L9.5 6" stroke="#fff" stroke-width="1.3" fill="none"/></svg><h3>Convenient</h3><p>Lorem ipsum dolor sit amet consectetur. Massa lacus imperdiet sed neque nunc diam pellentesque.</p></div>
    </section>

    <section class="about">
      <svg class="abs" style="left:211px;top:96px" width="45" height="45" viewBox="0 0 45 45"><path d="M45 0A45 45 0 000 45h45z" fill="#2a86cc"/></svg>
      <svg class="abs" style="left:230px;top:271px" width="26" height="26" viewBox="0 0 26 26"><path d="M0 0a26 26 0 0026 26V0z" fill="#2fb5a6"/></svg>
      <svg class="abs" style="left:400px;top:225px" width="14" height="14" viewBox="0 0 14 14"><path d="M14 0A14 14 0 010 14V0z" fill="#1f2a37"/></svg>
      <div class="photo" role="img" aria-label="Photo: gloved hand holding a spray bottle and cloth" style="left:138px;top:147px;width:117px;height:116px;background:linear-gradient(135deg,#dbe8f3,#4f9dd6)"></div>
      <div class="photo" role="img" aria-label="Photo: cleaner with a mop and blue cleaning trolley" style="left:261px;top:56px;width:164px;height:164px;background:linear-gradient(160deg,#e7ebee,#9aa6b3)"></div>
      <div class="photo" role="img" aria-label="Photo: cleaner mopping an open office floor" style="left:261px;top:226px;width:138px;height:137px;background:linear-gradient(160deg,#c8ccc9,#6f7a80)"></div>
      <div class="kicker"><i></i>WHO WE ARE</div>
      <h2>We Provide High Quality Cleaning Services</h2>
      <p style="top:160px">Lorem ipsum dolor sit amet consectetur. Massa lacus imperdiet sed neque nunc diam pellentesque. Amet vulputate vestibulum massa morbi viverra pharetra non nisi. Phasellus consectetur posuere urna vulputate. Cum a mauris facilisi non magna vestibulum pellentesque sagittis ut.</p>
      <p style="top:219px">Lorem ipsum dolor sit amet consectetur. Massa lacus imperdiet sed neque nunc diam pellentesque. Amet vulputate vestibulum massa morbi viverra pharetra non nisi. Phasellus consectetur posuere urna vulputate.</p>
      <div class="btn" style="left:450px;top:274px;width:95px;height:28px">Book Now</div>
    </section>

    <section class="services">
      <div class="mark" style="top:56px"></div>
      <h2 class="sec-title" style="top:86px">We Offer Different Services to Clean Your Area</h2>
      <div class="svc" style="left:138px;top:121px"><div class="pic" role="img" aria-label="Illustration of a bucket with cleaning supplies" style="background:linear-gradient(135deg,#5aa7e0,#f2c14e)"></div><h3>Residential Cleaning</h3><p>Lorem ipsum dolor sit amet consectetur. Massa lacus imperdiet sed neque nunc diam pellentesque.</p><div class="go"><svg width="10" height="8" viewBox="0 0 10 8"><path d="M0 4h8M5 1l3 3-3 3" stroke="#fff" stroke-width="1.4" fill="none"/></svg></div></div>
      <div class="svc" style="left:369px;top:121px"><div class="pic" role="img" aria-label="Illustration of a mop bucket and broom" style="background:linear-gradient(135deg,#f2c14e,#2a86cc)"></div><h3>Commercial Cleaning</h3><p>Lorem ipsum dolor sit amet consectetur. Massa lacus imperdiet sed neque nunc diam pellentesque.</p><div class="go"><svg width="10" height="8" viewBox="0 0 10 8"><path d="M0 4h8M5 1l3 3-3 3" stroke="#fff" stroke-width="1.4" fill="none"/></svg></div></div>
      <div class="svc" style="left:599px;top:121px"><div class="pic" role="img" aria-label="Illustration of a disinfectant spray bottle" style="background:linear-gradient(135deg,#e04758,#1e2a3a)"></div><h3>Antiviral Disinfection</h3><p>Lorem ipsum dolor sit amet consectetur. Massa lacus imperdiet sed neque nunc diam pellentesque.</p><div class="go"><svg width="10" height="8" viewBox="0 0 10 8"><path d="M0 4h8M5 1l3 3-3 3" stroke="#fff" stroke-width="1.4" fill="none"/></svg></div></div>
      <div class="svc" style="left:138px;top:317px"><div class="pic" role="img" aria-label="Illustration of a vacuum cleaner" style="background:linear-gradient(135deg,#2f4f9a,#e86b4a)"></div><h3>Construction Cleaning</h3><p>Lorem ipsum dolor sit amet consectetur. Massa lacus imperdiet sed neque nunc diam pellentesque.</p><div class="go"><svg width="10" height="8" viewBox="0 0 10 8"><path d="M0 4h8M5 1l3 3-3 3" stroke="#fff" stroke-width="1.4" fill="none"/></svg></div></div>
      <div class="promo">
        <div class="photo" role="img" aria-label="Photo: smiling cleaner in blue overalls holding a bucket of supplies and a mop" style="left:8px;top:-6px;width:103px;height:197px;background:linear-gradient(180deg,#c2d4ea 0%,#2c5fae 45%,#1c3f86 100%);border-radius:40px 40px 6px 6px"></div>
        <h3>Book a Trusted Cleaner Instantly</h3>
        <p>Lorem ipsum dolor sit amet consectetur. Massa lacus imperdiet sed neque nunc diam pellentesque.</p>
        <div class="btn" style="left:129px;top:108px;width:94px;height:28px">Book Now</div>
      </div>
    </section>

    <section class="how">
      <h2>How It Works</h2>
      <div class="dash" style="left:246px;width:280px"></div>
      <div class="dash" style="left:504px;width:280px"></div>
      <div class="step" style="left:141px"><div class="box"><svg width="16" height="16" viewBox="0 0 16 16"><rect x="1.5" y="2.5" width="13" height="12" rx="1.5" fill="none" stroke="#fff" stroke-width="1.3"/><path d="M1.5 6h13M5 1v3M11 1v3" stroke="#fff" stroke-width="1.3"/></svg></div><h3>Simply Schedule</h3><p>Lorem ipsum dolor sit amet consectetur. Massa lacus imperdiet.</p></div>
      <div class="step" style="left:399px"><div class="box"><svg width="16" height="16" viewBox="0 0 16 16"><path d="M14 2L7 9M7 9l-4 5h5l1-3z" stroke="#fff" stroke-width="1.3" fill="none"/></svg></div><h3>Clean</h3><p>Lorem ipsum dolor sit amet consectetur. Massa lacus imperdiet.</p></div>
      <div class="step" style="left:658px"><div class="box"><svg width="16" height="16" viewBox="0 0 16 16"><rect x="2" y="4" width="12" height="8" rx="2" fill="none" stroke="#fff" stroke-width="1.3"/><path d="M2 8h12" stroke="#fff" stroke-width="1.3"/></svg></div><h3>Relax</h3><p>Lorem ipsum dolor sit amet consectetur. Massa lacus imperdiet.</p></div>
    </section>

    <section class="reviews">
      <div class="mark" style="top:57px"></div>
      <h2 class="sec-title" style="top:86px">Testimonials</h2>
      <div class="arrow" style="left:138px"><svg width="10" height="8" viewBox="0 0 10 8"><path d="M10 4H2M5 1L2 4l3 3" stroke="#fff" stroke-width="1.4" fill="none"/></svg></div>
      <div class="review" style="left:154px"><div class="avatar" role="img" aria-label="Customer portrait photo" style="background:linear-gradient(160deg,#e4e6ee,#b9bdd0)"></div><h4>Daniel Ortiz</h4><small>Product Quality Engineer</small><div class="stars">★★★★★</div><p>Lorem ipsum dolor sit amet consectetur. Massa lacus imperdiet sed neque nunc diam pellentesque.</p><div class="tag"><i></i>Review</div></div>
      <div class="review" style="left:375px"><div class="avatar" role="img" aria-label="Customer portrait photo" style="background:linear-gradient(160deg,#d3cfc8,#6d5a4a)"></div><h4>Marcus Hale</h4><small>Lead Assurance Executive</small><div class="stars">★★★★★</div><p>Lorem ipsum dolor sit amet consectetur. Massa lacus imperdiet sed.</p><div class="tag"><i></i>Review</div></div>
      <div class="review" style="left:596px"><div class="avatar" role="img" aria-label="Customer portrait photo" style="background:linear-gradient(160deg,#6b5a46,#2a2520)"></div><h4>Elena Brooks</h4><small>Corporate Solutions Strategist</small><div class="stars">★★★★★</div><p>Lorem ipsum dolor sit amet consectetur. Massa lacus imperdiet sed neque nunc diam pellentesque.Lorem ipsum dolor sit amet consectetur. Massa lacus imperdiet sed neque nunc diam pellentesque.</p><div class="tag"><i></i>Review</div></div>
      <div class="arrow" style="left:789px"><svg width="10" height="8" viewBox="0 0 10 8"><path d="M0 4h8M5 1l3 3-3 3" stroke="#fff" stroke-width="1.4" fill="none"/></svg></div>
    </section>

    <section class="commit">
      <h2>We’re Committed to <em>200% CUSTOMER SATISFACTION</em> Each and Every Time</h2>
      <p>If you’re not happy with our work, we make it right!</p>
      <div class="btn" style="left:138px;top:132px;width:95px;height:28px">Book Now</div>
      <svg class="abs" style="left:614px;top:40px" width="120" height="90" viewBox="0 0 120 90"><g fill="none" stroke="#bfe6f3" stroke-width="1.5" opacity=".8"><circle cx="10" cy="30" r="3"/><circle cx="35" cy="52" r="7"/><circle cx="60" cy="35" r="4"/><circle cx="78" cy="70" r="6"/><circle cx="105" cy="15" r="10"/><circle cx="95" cy="45" r="3"/></g></svg>
    </section>

    <section class="foot">
      <div class="brand"><span class="dot"></span>BRIGHTWAY CLEANING</div>
      <div class="foot-links"><span>ABOUT US</span><span>SERVICE</span><span>SERVICE AREA</span><span>REVIEW</span><span>PRICING</span><span>CONTACT US</span></div>
      <div class="hr" style="top:157px"></div>
      <div class="contact" style="left:268px;top:166px">
        <div class="ico"><svg width="11" height="9" viewBox="0 0 11 9"><rect x=".5" y=".5" width="10" height="8" fill="none" stroke="#2a86cc"/><path d="M.5 .5l5 4 5-4" fill="none" stroke="#2a86cc"/></svg></div>
        <div><b>MAIL US</b><span>hello@brightwaycleaning.com</span></div>
      </div>
      <div class="vline" style="left:418px;top:166px"></div>
      <div class="contact" style="left:436px;top:166px">
        <div class="ico"><svg width="11" height="11" viewBox="0 0 11 11"><circle cx="5.5" cy="5.5" r="5" fill="#2a86cc"/><path d="M5.5 2.5v3l2 1.3" stroke="#fff" fill="none"/></svg></div>
        <div><b>BUSINESS HOURS</b><span>9:00 AM - 7:00 PM Mon-Sat</span></div>
      </div>
      <div class="vline" style="left:583px;top:166px"></div>
      <div class="contact" style="left:600px;top:166px">
        <div class="ico"><svg width="11" height="11" viewBox="0 0 24 24"><path d="M6.6 10.8a15 15 0 006.6 6.6l2.2-2.2c.3-.3.7-.4 1-.2 1.1.4 2.3.6 3.6.6.6 0 1 .4 1 1V20c0 .6-.4 1-1 1C10.6 21 3 13.4 3 4c0-.6.4-1 1-1h3.5c.6 0 1 .4 1 1 0 1.3.2 2.5.6 3.6.1.3 0 .7-.2 1z" fill="#2a86cc"/></svg></div>
        <div><b>CALL US TODAY</b><span>(555) 014-2290</span></div>
      </div>
      <div class="hr" style="top:203px"></div>
      <div class="copy">© 2024. All rights reserved</div>
    </section>
  </main>

  <div class="abs" role="img" aria-label="Photo: cleaner in red shirt and blue overalls pushing a cleaning trolley" style="left:740px;top:2566px;width:182px;height:246px;background:linear-gradient(180deg,#d9453f 0%,#c83a3a 30%,#2a4f9a 55%,#1d3c7e 100%);border-radius:60px 60px 10px 10px"></div>

  <div class="abs thanks">Thanks for Watching</div>
</div>
</body>
</html>
```